Mobile Laboratory Design Project Needed

We need a professional brochure made. We are a mobile laboratory service company providing venipuncture, laboratory testing and laboratory consultation services to nursing homes. We would like the brochure made 8 x 11 with the last page being a contact us page and a place to put two business cards.

Target Market(s)

Nursing Home Administrators and Directors of Nursing

Industry/Entity Type

Medical

Colors
0054AA
0677BA
7BADD7
CADEEF
E8F1F8

```html
<!DOCTYPE html>
<html lang="en">
<head>
<meta charset="utf-8">
<title>Crestline Mobile Labs – Trifold Brochure</title>
<link href="https://fonts.googleapis.com/css2?family=Merriweather:wght@400;700&family=Montserrat:wght@400;500;700;800&display=swap" rel="stylesheet">
<style>
  :root{
    --blue-deep:#0054AA;
    --blue-mid:#0677BA;
    --blue-soft:#7BADD7;
    --blue-pale:#CADEEF;
    --blue-mist:#E8F1F8;
    --ink:#333a44;
    --night:#0b0d14;
    --stage:#2a2a2a;
    --white:#ffffff;
  }
  *{box-sizing:border-box;margin:0;padding:0}
  html,body{width:809px;height:1200px;overflow:hidden}
  body{background:var(--stage);font-family:'Montserrat',sans-serif;position:relative}
  .sheet{position:absolute;left:99px;width:611px;height:472px;overflow:hidden;box-shadow:0 10px 24px rgba(0,0,0,.45)}
  .sheet--outside{top:90px}
  .sheet--inside{top:634px}
  .panel{position:absolute;top:0;height:100%;width:204px}
  .panel--1{left:0}.panel--2{left:204px}.panel--3{left:408px;width:203px}
  .abs{position:absolute}
  .heading{font-family:'Merriweather',serif;font-weight:700;font-size:13.5px;line-height:16px;color:var(--ink)}
  .heading--light{color:var(--white)}
  .heading--bar{padding-left:8px;border-left:1.5px solid currentColor}
  .heading .thin{font-weight:400;display:block}
  .body,.service__text{font-size:8.6px;line-height:12.35px;text-align:justify;letter-spacing:-.1px;hyphens:auto;-webkit-hyphens:auto;color:var(--ink)}
  .body--light{color:var(--white)}
  .photo{position:absolute}
  .photo--round{border-radius:50%;border:3px solid var(--blue-soft)}
  .wave{position:absolute;left:0;top:0}
  .card-slot{position:absolute;left:14px;width:175px;height:111px;border:1px solid #c8cbd0;border-radius:4px;background:linear-gradient(#f3f4f5,#e9eaec)}
  .card-slot span{position:absolute;inset:0;display:flex;align-items:center;justify-content:center;font-family:'Merriweather',serif;font-size:9.5px;color:#111}
  .card-slot svg{position:absolute;inset:0}
  .contact{font-size:9px;line-height:11.3px;color:var(--white);position:absolute;left:40px;width:160px}
  .contact svg{position:absolute;left:-13px;top:1px}
  .cover-title{position:absolute;left:27px;top:325px;color:var(--white);font-size:19.5px;line-height:23px;font-weight:400;letter-spacing:.2px}
  .cover-title b{font-weight:800;font-size:24px;display:block;line-height:24px}
  .cover-url{position:absolute;left:27px;top:426px;width:145px;height:23px;background:#141414;color:var(--white);font-size:9px;display:flex;align-items:center;justify-content:center}
  .brand{position:absolute;left:56px;top:40px;width:92px;text-align:center;color:var(--blue-soft);font-family:'Montserrat',sans-serif;font-weight:700;font-size:12px;letter-spacing:2px}
  .service{position:absolute;left:23px;width:158px}
  .service__icon{position:absolute;left:0;top:0;width:41px;height:41px;border:1.5px solid var(--white);border-radius:50%}
  .service__title{position:absolute;left:51px;width:104px;font-family:'Merriweather',serif;font-weight:700;font-size:13px;line-height:16px;color:var(--white);padding-bottom:3px;border-bottom:1px solid var(--blue-soft)}
  .service__text{position:absolute;left:0;width:155px;color:var(--white)}
  .checklist{position:absolute;left:23px;top:284px;list-style:none}
  .checklist li{font-size:10px;font-weight:500;color:var(--ink);height:18.1px;display:flex;align-items:center;gap:5px}
</style>
</head>
<body>

<section class="sheet sheet--outside" style="background:linear-gradient(90deg,#d6d8db,#eeeff1 33%,#e4e5e8 34%,#f6f6f7 66%)">
  <svg class="wave" width="611" height="472" viewBox="0 0 611 472" aria-hidden="true">
    <path d="M0,222 C70,205 150,214 204,250 C255,286 290,310 330,312 C372,314 420,290 480,262 L611,250 L611,472 L0,472Z" fill="var(--blue-mid)"/>
    <path d="M0,248 C70,222 150,228 204,262 C255,294 290,318 330,318 C372,318 420,296 480,275 L611,265 L611,472 L0,472Z" fill="var(--blue-deep)"/>
  </svg>

  <div class="panel panel--1">
    <h2 class="abs heading heading--bar" style="left:24px;top:26px"><span class="thin">Laboratory and</span>Phlebotomy Services</h2>
    <p class="abs body" style="left:24px;top:69px;width:155px">Crestline Mobile Labs is positively impacting the lives in our community through fast and accurate venipuncture and laboratory testing. Our CLIA licensed and Joint Commission certified laboratory performs testing in the areas of Hematology, Chemistry, Urinalysis, Immunohematology, Coagulation and Microbiology.</p>
    <div class="photo photo--round" role="img" aria-label="Photo of scientists working in a clinical laboratory" style="left:101px;top:202px;width:94px;height:94px;background:radial-gradient(circle at 40% 40%,#c9b79a,#6e6152 60%,#3b352e)"></div>
    <h2 class="abs heading heading--light heading--bar" style="left:24px;top:284px">Who We Are</h2>
    <p class="abs body body--light" style="left:24px;top:306px;width:155px;font-weight:500">Highly qualified and motivated Laboratory professionals</p>
    <p class="abs body body--light" style="left:24px;top:336px;width:155px">The owners of CML collectively have over 50 years of experience operating and running clinical laboratories across the United States. The company consists of Medical Doctors, CLIA Directors, Medical Technologists and Phlebotomists that are considered experts in their fields.</p>
  </div>

  <div class="panel panel--2">
    <div class="card-slot" style="top:23px">
      <svg width="175" height="111" aria-hidden="true"><g stroke="#888" stroke-width=".7"><path d="M15,17 L27,29M160,17 L148,29M15,94 L27,82M160,94 L148,82"/></g></svg>
      <span>Place for Business Card</span>
    </div>
    <div class="card-slot" style="top:149px">
      <svg width="175" height="111" aria-hidden="true"><g stroke="#888" stroke-width=".7"><path d="M15,17 L27,29M160,17 L148,29M15,94 L27,82M160,94 L148,82"/></g></svg>
      <span>Place for Business Card</span>
    </div>
    <h2 class="abs heading heading--light heading--bar" style="left:30px;top:338px">Contact us</h2>
    <p class="contact" style="top:364px">
      <svg width="9" height="10" viewBox="0 0 9 10" aria-hidden="true"><path d="M4.5,9.5 C2,6 1,4.5 1,3.5 A3.5,3.5 0 0 1 8,3.5 C8,4.5 7,6 4.5,9.5Z" fill="none" stroke="#fff" stroke-width=".8"/><circle cx="4.5" cy="3.6" r="1.2" fill="none" stroke="#fff" stroke-width=".8"/></svg>
      4180 Harbor Ridge Drive, Suite 210, Fairview, Oregon 97024.</p>
    <p class="contact" style="top:404px">
      <svg width="9" height="8" viewBox="0 0 9 8" aria-hidden="true"><rect x=".5" y="1" width="8" height="6" fill="none" stroke="#fff" stroke-width=".8"/><path d="M.5,1 L4.5,4.5 L8.5,1" fill="none" stroke="#fff" stroke-width=".8"/></svg>
      admin@crestlinelabs.com</p>
    <p class="contact" style="top:421px">
      <svg width="9" height="9" viewBox="0 0 9 9" aria-hidden="true"><path d="M2,1 L3.5,1 L4,3 L3,4 C3.6,5.3 4.2,5.9 5,6.2 L6,5.2 L8,5.7 L8,7.3 C5,8 1.2,4.5 2,1Z" fill="none" stroke="#fff" stroke-width=".8"/></svg>
      (555) 014-2290</p>
    <p class="contact" style="top:438px">
      <svg width="9" height="9" viewBox="0 0 9 9" aria-hidden="true"><g fill="none" stroke="#fff" stroke-width=".7"><circle cx="4.5" cy="4.5" r="3.8"/><ellipse cx="4.5" cy="4.5" rx="1.6" ry="3.8"/><path d="M.7,4.5H8.3"/></g></svg>
      www.<b>crestlinelabs</b>.com</p>
  </div>

  <div class="panel panel--3" style="background:linear-gradient(180deg,var(--night) 0%,#1a1410 40%,#3a2410 52%,var(--blue-deep) 60%,var(--blue-deep) 100%)">
    <div class="brand">CML
      <div style="width:60px;height:60px;margin:8px auto 0;border:2.5px solid var(--blue-mid);border-radius:50%"></div>
      <div style="font-size:8px;letter-spacing:1px;margin-top:6px;font-weight:700">CRESTLINE MOBILE LABS</div>
    </div>
    <div class="photo photo--round" role="img" aria-label="Photo of a doctor talking with a seated patient" style="left:75px;top:157px;width:130px;height:140px;background:linear-gradient(135deg,#e9edf1,#cfd6de 45%,#e39b8a 80%,#b86e5f)"></div>
    <div class="photo photo--round" role="img" aria-label="Photo of blood sample tubes on a lab request form" style="left:8px;top:212px;width:88px;height:88px;background:linear-gradient(135deg,#f1e6e6,#b3353e 55%,#5a1218)"></div>
    <h1 class="cover-title">LABORATORY<b>RESULTS</b>THAT YOU CAN<b>TRUST</b></h1>
    <div class="cover-url">www.<b>crestlinelabs</b>.com</div>
  </div>
</section>

<section class="sheet sheet--inside">
  <div class="panel panel--1" style="background:linear-gradient(180deg,#eef3f6,#f8fafb 45%,#fff)">
    <h2 class="abs heading heading--bar" style="left:24px;top:27px">Our Mission</h2>
    <p class="abs body" style="left:24px;top:49px;width:155px">There's a notion that to be successful you have to be a huge conglomerate. But we know there is a better way to grow and truly serve the community. That is by making sure what is good for the bottom line is also good for the customer! That is why we created an ecosystem that unites mobile phlebotomy, the clinical laboratory, analytics and machine learning to deliver optimum clinical laboratory services to the communities we serve.</p>
    <div class="photo" role="img" aria-label="Photo of a doctor and a patient looking at a tablet together" style="left:0;top:245px;width:204px;height:227px;background:linear-gradient(160deg,#f4f6f8 0%,#d9dde2 35%,#5a4a44 60%,#304a78 85%,#e7e9ec)"></div>
  </div>

  <div class="panel panel--2" style="background:var(--blue-deep)">
    <div class="service" style="top:27px">
      <span class="service__icon"><svg width="38" height="38" viewBox="0 0 38 38" aria-hidden="true"><g fill="none" stroke="#fff" stroke-width="1"><path d="M10,27 L22,15 L25,18 L13,30Z"/><path d="M8,29 L10,27"/><path d="M27,9 C24,13 23,15 23,16.5 A4,4 0 0 0 31,16.5 C31,15 30,13 27,9Z"/></g></svg></span>
      <h3 class="service__title" style="top:11px">Venipuncture</h3>
      <p class="service__text" style="top:52px">Our skilled phlebotomists perform venipuncture with precision and care, ensuring minimal discomfort for our clients.</p>
    </div>
    <div class="service" style="top:139px">
      <span class="service__icon"><svg width="38" height="38" viewBox="0 0 38 38" aria-hidden="true"><g fill="none" stroke="#fff" stroke-width="1"><path d="M14,9 H20 M15.5,9 V17 L10,27 H24 L18.5,17 V9"/><rect x="24" y="11" width="4" height="16" rx="2"/></g></svg></span>
      <h3 class="service__title" style="top:4px">Laboratory Testing</h3>
      <p class="service__text" style="top:56px">With our advanced laboratory equipment, we conduct a wide range of tests accurately and efficiently.</p>
    </div>
    <div class="service" style="top:253px">
      <span class="service__icon"><svg width="38" height="38" viewBox="0 0 38 38" aria-hidden="true"><g fill="none" stroke="#fff" stroke-width="1"><circle cx="12" cy="14" r="3"/><circle cx="26" cy="14" r="3"/><path d="M7,28 C7,22 17,22 17,28 M21,28 C21,22 31,22 31,28"/><rect x="15" y="7" width="8" height="5" rx="1"/></g></svg></span>
      <h3 class="service__title" style="top:4px">Laboratory Consultation</h3>
      <p class="service__text" style="top:56px">Our healthcare experts provide professional medical consultation and guidance for individuals and healthcare organizations.</p>
    </div>
    <div class="photo" role="img" aria-label="Photo of gloved hands drawing blood from a patient's arm" style="left:22px;top:363px;width:158px;height:88px;background:linear-gradient(120deg,#f5f3f1,#c89c88 45%,#3fa7e0 75%,#2a6fbf)"></div>
  </div>

  <div class="panel panel--3" style="background:linear-gradient(180deg,#f7f7f8,#e8e9eb)">
    <h2 class="abs heading heading--bar" style="left:23px;top:27px">Test Menu</h2>
    <h3 class="abs heading" style="left:23px;top:50px;font-size:11.5px">Crestline Mobile Labs</h3>
    <p class="abs body" style="left:23px;top:72px;width:155px">Crestline Mobile Labs has a wide range of laboratory testing that covers the following disease states: Anemia, Bone/Skeleton, Cardiac, Diabetes, Drugs of Abuse, General Chemistry, Hepatic, Immunosuppressant Drugs, Infectious Disease, Inflammatory, Lipids, Microbiology, Mycology Nutritional Assessment, Oncology, Pancreatic, Parasitology, Prenatal, Renal, Reproductive Endocrinology, Respiratory, Sepsis, Spinal, Therapeutic Drug Monitoring, Metabolic, Toxicology, Urinalysis and Virology.</p>
    <ul class="checklist">
      <li><svg width="10" height="10" viewBox="0 0 10 10" aria-hidden="true"><circle cx="5" cy="5" r="4.3" fill="none" stroke="var(--blue-deep)" stroke-width=".9"/><path d="M3,5.2 L4.4,6.5 L7,3.8" fill="none" stroke="var(--blue-deep)" stroke-width=".9"/></svg>Clinical Chemistry</li>
      <li><svg width="10" height="10" viewBox="0 0 10 10" aria-hidden="true"><circle cx="5" cy="5" r="4.3" fill="none" stroke="var(--blue-deep)" stroke-width=".9"/><path d="M3,5.2 L4.4,6.5 L7,3.8" fill="none" stroke="var(--blue-deep)" stroke-width=".9"/></svg>Parisitology</li>
      <li><svg width="10" height="10" viewBox="0 0 10 10" aria-hidden="true"><circle cx="5" cy="5" r="4.3" fill="none" stroke="var(--blue-deep)" stroke-width=".9"/><path d="M3,5.2 L4.4,6.5 L7,3.8" fill="none" stroke="var(--blue-deep)" stroke-width=".9"/></svg>Immunohematology</li>
      <li><svg width="10" height="10" viewBox="0 0 10 10" aria-hidden="true"><circle cx="5" cy="5" r="4.3" fill="none" stroke="var(--blue-deep)" stroke-width=".9"/><path d="M3,5.2 L4.4,6.5 L7,3.8" fill="none" stroke="var(--blue-deep)" stroke-width=".9"/></svg>Mycology</li>
      <li><svg width="10" height="10" viewBox="0 0 10 10" aria-hidden="true"><circle cx="5" cy="5" r="4.3" fill="none" stroke="var(--blue-deep)" stroke-width=".9"/><path d="M3,5.2 L4.4,6.5 L7,3.8" fill="none" stroke="var(--blue-deep)" stroke-width=".9"/></svg>Urinalysis</li>
      <li><svg width="10" height="10" viewBox="0 0 10 10" aria-hidden="true"><circle cx="5" cy="5" r="4.3" fill="none" stroke="var(--blue-deep)" stroke-width=".9"/><path d="M3,5.2 L4.4,6.5 L7,3.8" fill="none" stroke="var(--blue-deep)" stroke-width=".9"/></svg>Microbiology</li>
      <li><svg width="10" height="10" viewBox="0 0 10 10" aria-hidden="true"><circle cx="5" cy="5" r="4.3" fill="none" stroke="var(--blue-deep)" stroke-width=".9"/><path d="M3,5.2 L4.4,6.5 L7,3.8" fill="none" stroke="var(--blue-deep)" stroke-width=".9"/></svg>Virology</li>
      <li><svg width="10" height="10" viewBox="0 0 10 10" aria-hidden="true"><circle cx="5" cy="5" r="4.3" fill="none" stroke="var(--blue-deep)" stroke-width=".9"/><path d="M3,5.2 L4.4,6.5 L7,3.8" fill="none" stroke="var(--blue-deep)" stroke-width=".9"/></svg>Tumor Markers</li>
      <li><svg width="10" height="10" viewBox="0 0 10 10" aria-hidden="true"><circle cx="5" cy="5" r="4.3" fill="none" stroke="var(--blue-deep)" stroke-width=".9"/><path d="M3,5.2 L4.4,6.5 L7,3.8" fill="none" stroke="var(--blue-deep)" stroke-width=".9"/></svg>Hematology</li>
    </ul>
  </div>
</section>

</body>
</html>
```